New Property management company business cards

Looking for a new business card, to reflect new younger ownership
Card should be clean, simple and professional but with a modern layout that is conveys our new logo and business model

Key aspects of the business:

Property Management
Facility Maintenance
Project Management
Tenant Improvements

Mailing Address:
PO BOX 7186
Brenton CA, 95371

Phone: 209-614-8837
Direct: 209-614-8831

Doyle Farrant
President

Target Market(s)

Commercial property owners

Industry/Entity Type

Real Estate property management

Contact Information for Business Card

Open to all designs but lean toward vertical layouts

Requirements
Must have
• Logo and space to customize name and contact info

```html
<!DOCTYPE html>
<html lang="en">
<head>
<meta charset="utf-8">
<title>Alderic – Business Card</title>
<link rel="stylesheet" href="https://fonts.googleapis.com/css2?family=Montserrat:wght@400;700&display=swap">
<style>
  :root {
    --teal: #20ada7;
    --teal-deep: #2e9793;
    --ink: #33323f;
    --white: #ffffff;
    --backdrop: #eeeeee;
  }
  * { box-sizing: border-box; margin: 0; padding: 0; }
  html, body {
    width: 1200px; height: 1200px; overflow: hidden;
    background: var(--backdrop);
    font-family: "Montserrat", sans-serif;
  }
  .card {
    position: absolute;
    left: 150px; width: 898px; height: 525px;
    box-shadow: 0 3px 8px rgba(0,0,0,0.18);
    overflow: hidden;
  }
  .card--front { top: 45px; background: var(--teal); }
  .card--back { top: 619px; background: var(--white); display: flex; align-items: center; justify-content: center; }
  .card__shapes { position: absolute; inset: 0; width: 100%; height: 100%; }
  .person { position: absolute; left: 60px; top: 150px; color: var(--white); }
  .person__name { font-size: 36px; font-weight: 700; letter-spacing: 0.5px; line-height: 1; }
  .person__title { font-size: 22px; font-weight: 400; margin-top: 14px; }
  .contact { list-style: none; margin-top: 22px; font-size: 22px; letter-spacing: 0.6px; }
  .contact li { position: relative; padding-left: 30px; line-height: 34.5px; }
  .contact svg { position: absolute; left: 0; top: 11px; width: 13px; height: 13px; fill: var(--white); }
  .brand { display: flex; align-items: center; gap: 12px; color: var(--ink); font-weight: 700; }
  .brand__mark { background: var(--teal); flex: none; }
  .brand--small { position: absolute; left: 643px; top: 240px; font-size: 38px; letter-spacing: 3px; }
  .brand--small .brand__mark { width: 26px; height: 26px; }
  .brand--large { font-size: 72px; letter-spacing: 6px; gap: 22px; }
  .brand--large .brand__mark { width: 52px; height: 52px; }
</style>
</head>
<body>
  <section class="card card--front">
    <svg class="card__shapes" viewBox="0 0 718 420" preserveAspectRatio="none" aria-hidden="true">
      <polygon fill="var(--teal-deep)" points="145,0 465,0 530,47 437,209"/>
      <polygon fill="var(--teal-deep)" points="145,420 465,420 530,373 437,209"/>
      <polygon fill="var(--ink)" points="465,0 650,0 718,47 530,47"/>
      <polygon fill="var(--ink)" points="465,420 650,420 718,373 530,373"/>
      <polygon fill="var(--white)" points="530,47 718,47 718,373 530,373 437,209"/>
    </svg>
    <div class="person">
      <h1 class="person__name">DOYLE FARRANT</h1>
      <p class="person__title">President</p>
      <ul class="contact">
        <li><svg viewBox="0 0 24 24"><path d="M6.6 10.8a15 15 0 0 0 6.6 6.6l2.2-2.2a1 1 0 0 1 1-.25 11.4 11.4 0 0 0 3.6.57 1 1 0 0 1 1 1V20a1 1 0 0 1-1 1A17 17 0 0 1 3 4a1 1 0 0 1 1-1h3.5a1 1 0 0 1 1 1c0 1.25.2 2.45.57 3.57a1 1 0 0 1-.25 1z"/></svg>209-614-8837</li>
        <li><svg viewBox="0 0 24 24"><path d="M6.6 10.8a15 15 0 0 0 6.6 6.6l2.2-2.2a1 1 0 0 1 1-.25 11.4 11.4 0 0 0 3.6.57 1 1 0 0 1 1 1V20a1 1 0 0 1-1 1A17 17 0 0 1 3 4a1 1 0 0 1 1-1h3.5a1 1 0 0 1 1 1c0 1.25.2 2.45.57 3.57a1 1 0 0 1-.25 1z"/></svg>209-614-8831</li>
        <li><svg viewBox="0 0 24 24"><path d="M12 3 1 12h3v9h6v-6h4v6h6v-9h3z"/></svg>PO BOX 7186</li>
        <li>Brenton CA, 95371</li>
      </ul>
    </div>
    <div class="brand brand--small"><span class="brand__mark"></span><span class="brand__name">ALDERIC</span></div>
  </section>

  <section class="card card--back">
    <div class="brand brand--large"><span class="brand__mark"></span><span class="brand__name">ALDERIC</span></div>
  </section>
</body>
</html>
```